Pull Up Banner Design 85cm X200cm

The pull up banner is intended for branding and services awareness purposes, and to be used at exhibition and conference. Please refer to the websites below for more information
1. https://www.brivanta.online/
2. https://www.brivanta.online/landing-page
3. https://blog.brivanta.online/faq-for-client/
4. https://blog.brivanta.online/faq-for-advisor/

Ideally, the banner will lead potential users both young entrepreneurs and online business owners (as clients) to Brivanta marketplace, and also professional services providers like accountants and finance advisors and consultants (as advisors) to sign up with the platform. (Like PixelHarbor marketplace)

Target Market(s)

Business users and accountants aged between 25 to 44 yrs old

Requirements
Must have
• website address (www.brivanta.online)
• and
• company logo "Brivanta" as attached

```html
<!DOCTYPE html>
<html lang="en">
<head>
<meta charset="utf-8">
<title>Brivanta Pull Up Banner</title>
<link rel="stylesheet" href="https://fonts.googleapis.com/css2?family=Fira+Sans:wght@400;500;600&family=Fira+Sans+Condensed:wght@500;600&display=swap">
<style>
  :root {
    --page-bg: #d9dbde;
    --banner-top: #f7f8f9;
    --banner-bottom: #e9eaec;
    --brand-blue: #1a6fb5;
    --band-blue: #128ad0;
    --band-blue-deep: #0f78bd;
    --ink-dark: #48494c;
    --wedge-dark: #4d4e51;
    --tile-teal: #6cbdb7;
    --white: #ffffff;
  }
  * { margin: 0; padding: 0; box-sizing: border-box; }
  html, body {
    width: 1200px;
    height: 1062px;
    overflow: hidden;
    background: var(--page-bg);
  }
  .canvas {
    position: relative;
    width: 1200px;
    height: 1062px;
  }
  .banner-frame {
    position: absolute;
    left: 375px;
    top: 16px;
    width: 450px;
    height: 1030px;
    overflow: hidden;
  }
  .banner {
    position: absolute;
    left: 0;
    top: 0;
    width: 401px;
    height: 917px;
    transform: scale(1.1222);
    transform-origin: 0 0;
    background: linear-gradient(180deg, var(--banner-top), var(--banner-bottom));
    font-family: "Fira Sans", "Open Sans", sans-serif;
    color: var(--ink-dark);
  }
  .banner-shapes {
    position: absolute;
    left: 0;
    top: 0;
    width: 401px;
    height: 917px;
  }
  .line {
    position: absolute;
    left: 0;
    width: 401px;
    text-align: center;
    white-space: nowrap;
  }
  .brand-mark {
    position: absolute;
    left: 168px;
    top: 26px;
    width: 66px;
    height: 66px;
    border-radius: 50%;
    background: var(--brand-blue);
  }
  .brand-name {
    top: 102px;
    font-size: 37px;
    line-height: 44px;
    font-weight: 500;
    color: var(--brand-blue);
    letter-spacing: 0.5px;
  }
  .band-services {
    top: 220px;
    font-family: "Fira Sans Condensed", "Fira Sans", sans-serif;
    font-size: 25px;
    line-height: 30px;
    font-weight: 500;
    color: var(--white);
  }
  .headline {
    top: 379px;
    font-family: "Fira Sans Condensed", "Fira Sans", sans-serif;
    font-size: 39px;
    line-height: 44px;
    font-weight: 600;
    color: var(--brand-blue);
  }
  .tagline {
    top: 422px;
    font-family: "Fira Sans Condensed", "Fira Sans", sans-serif;
    font-size: 27px;
    line-height: 31px;
    font-weight: 500;
    color: var(--ink-dark);
  }
  .accent { color: var(--brand-blue); }
  .step-art {
    position: absolute;
    width: 106px;
    height: 106px;
    border-radius: 50%;
    background: var(--tile-teal);
  }
  .step-caption {
    position: absolute;
    width: 170px;
    text-align: center;
    font-size: 13.5px;
    line-height: 16.5px;
    font-weight: 500;
    color: var(--ink-dark);
  }
  .website {
    top: 877px;
    font-size: 24px;
    line-height: 30px;
    letter-spacing: 0.6px;
    color: var(--ink-dark);
  }
  .website strong { color: var(--brand-blue); font-weight: 600; }
</style>
</head>
<body>
<div class="canvas">
  <div class="banner-frame">
    <div class="banner">
      <svg class="banner-shapes" viewBox="0 0 401 917" aria-hidden="true">
        <defs>
          <linearGradient id="band-fill" x1="0" y1="1" x2="1" y2="0">
            <stop offset="0" stop-color="var(--band-blue-deep)"/>
            <stop offset="1" stop-color="var(--band-blue)"/>
          </linearGradient>
        </defs>
        <polygon class="wedge" points="0,140 148,185 0,227" fill="var(--wedge-dark)"/>
        <polygon class="service-band" points="0,236 401,125 401,305 0,398" fill="url(#band-fill)"/>
        <rect class="base-strip" x="0" y="910" width="401" height="7" fill="var(--brand-blue)"/>
      </svg>

      <div class="brand-mark"></div>
      <p class="line brand-name">Brivanta</p>

      <div role="img" aria-label="Faint illustration of advisors working at a desk behind the services band" style="position:absolute;left:0;top:0;width:0;height:0;"></div>
      <p class="line band-services">Tax, Accounting,<br>Financials, Business Advisory,<br>Fundraising Services</p>

      <h1 class="line headline">BRIVANTA</h1>
      <p class="line tagline">matches you with the right<br>Advisors <span class="accent">Online!</span></p>

      <div class="step-art" style="left:64px;top:504px;" role="img" aria-label="Illustration of a client posting business needs on a tablet"></div>
      <p class="step-caption" style="left:35px;top:619px;">Tell us your<br>business needs &amp;<br>post a job online</p>

      <div class="step-art" style="left:236px;top:504px;" role="img" aria-label="Illustration of a client chatting with an advisor on a laptop"></div>
      <p class="step-caption" style="left:206px;top:619px;">Agree terms and<br>appoint your Advisor<br>through our Chat tool</p>

      <div class="step-art" style="left:53px;top:699px;" role="img" aria-label="Illustration of a client connected to several advisors"></div>
      <p class="step-caption" style="left:21px;top:812px;">We'll match<br>you with 3 or more<br>Advisors</p>

      <div class="step-art" style="left:234px;top:699px;" role="img" aria-label="Illustration of a laptop showing a job progress dashboard"></div>
      <p class="step-caption" style="left:202px;top:812px;">Track your job<br>progress from your<br>Dashboard</p>

      <p class="line website">www.<strong>brivanta</strong>.online</p>
    </div>
  </div>
</div>
</body>
</html>
```